New, High-Tech Website for Venture Z - A Product Development Company

Venture Z is located in Silicon Valley, CA. We help companies build products from start to finish and everywhere in between. We build teams with top talent based on our customer's needs. We need a BRAND NEW website that looks innovative, fresh, new & modern. We want our website to impress companies that will hire us, as well as developers, designers, product people, etc.

The design is very important!

Target Market(s)

Small companies, entrepreneurs, anyone who needs help building a product or finding top talent

Industry/Entity Type

Tech

Coding

Coded - Design and coding required

Font styles to use
Sans Serif

Requirements
Must have
• Our logo (attached) and colors that look good with the logo.

**UPDATE - Site should be fully coded for WordPress and be MOBILE FRIENDLY. (Responsive Designs)
Nice to have
• We would love to see your ideas and if you have any other cool ideas to make our site POP and look attractive.

Please also let us know the following when you submit your design (in the notes section)!

1) Are we able to use any illustrations or images you provided legally? Would we need to pay any additional fees for images or illustrations?  If so, how much per picture/illustration?

2) If we choose your design, do your services include deploying the design to our Wordpress site?  Or, do you charge extra for this and how much?

3) If we choose your design, will this include any other page designs?  If so, how many?

4) If we choose your design, how much will you charge to design and implement other pages for us (like our contact us page, careers page, site map page, etc.) so our website looks cohesive?

5) What is your turnaround time for further page designs and implementations to the site?

6) Can you design AND implement surveys and/or custom questionnaires? What is the cost?
Should not have
• Nothing too "corporate" looking. For example, no images with men in suits around a large conference room because this doesn't represent who we are. We are more looking for images of people working - small startup company style.

Really cool, high tech illustrations are good too.

```html
<!DOCTYPE html>
<html lang="en">
<head>
<meta charset="utf-8">
<title>Venture Z – Product Development</title>
<link rel="stylesheet" href="https://fonts.googleapis.com/css2?family=Ubuntu:wght@300;400;500;700&display=swap">
<style>
:root{
  --teal:#29b3c9;
  --teal-light:#36cdc4;
  --teal-pale:#e9f6f9;
  --green:#1b7a6d;
  --ink:#1c1f26;
  --text:#5a5f66;
  --muted:#8a9097;
  --footer:#262a36;
  --white:#ffffff;
}
*{box-sizing:border-box;margin:0;padding:0}
html,body{width:1200px;height:4773px;overflow:hidden}
body{font-family:"Ubuntu",sans-serif;color:var(--text);background:var(--white);position:relative}
.abs{position:absolute}
.btn{position:absolute;display:flex;align-items:center;justify-content:center;border-radius:24px;font-size:13px;font-weight:500}
.btn-fill{background:var(--teal-light);color:var(--white)}
.btn-line{border:2px solid var(--teal-light);color:var(--teal);background:var(--white)}
.btn-white{background:var(--white);color:var(--teal)}
.h2{position:absolute;left:0;width:1200px;text-align:center;font-size:38px;font-weight:300;color:var(--teal)}
.h2 b{font-weight:700;color:var(--ink)}
.lead{position:absolute;left:270px;width:660px;text-align:center;font-size:13px;line-height:24px;color:var(--text)}

/* header */
.site-header{position:absolute;left:0;top:0;width:1200px;height:107px;background:var(--white)}
.brand{position:absolute;left:58px;top:30px;display:flex;align-items:center;gap:10px;font-size:20px;font-weight:700;color:var(--teal)}
.brand i{width:26px;height:26px;border-radius:50%;background:var(--teal);display:block}
.nav{position:absolute;top:40px;left:318px;display:flex;align-items:center;gap:30px;font-size:13px;color:var(--ink)}
.nav .home{width:30px;height:30px;border-radius:50%;border:1px solid var(--teal-light);display:flex;align-items:center;justify-content:center}

/* hero */
.hero{position:absolute;left:0;top:107px;width:1200px;height:489px;background:linear-gradient(100deg,#6cc6de 0%,#8fd8ea 45%,#5bbcd6 100%)}
.hero-title{position:absolute;top:168px;width:1200px;text-align:center;font-size:48px;font-weight:500;color:var(--white)}
.hero-sub{position:absolute;top:236px;width:1200px;text-align:center;font-size:18px;color:var(--white)}
.intro-card{position:absolute;left:157px;top:528px;width:884px;height:166px;background:var(--white);box-shadow:0 6px 24px rgba(0,0,0,.08);text-align:center}
.intro-card h3{margin-top:28px;font-size:22px;font-weight:500;color:var(--ink)}
.intro-card h3 span{color:var(--teal);margin-left:8px}
.intro-card p{margin:16px auto 0;width:760px;font-size:12px;line-height:23px;color:var(--muted)}

/* work with */
.work-title{position:absolute;left:157px;top:780px;font-size:38px;font-weight:300;color:var(--teal)}
.work-title b{font-weight:700;color:var(--ink)}
.work-list{position:absolute;left:157px;top:848px;width:440px;list-style:none}
.work-list li{position:relative;padding-left:22px;font-size:12.5px;line-height:22px;color:var(--text);margin-bottom:22px}
.work-list li svg{position:absolute;left:0;top:5px}
.work-photo{position:absolute;left:644px;top:791px;width:460px;height:390px;border-radius:50%;background:radial-gradient(circle at 45% 45%,#6f7c86 0%,#b9c4cc 40%,#e6edf1 72%,#ffffff 100%)}

/* excite */
.excite{position:absolute;left:0;top:1269px;width:1200px;height:376px;background:#f6f9fa}
.icon-card{position:absolute;top:130px;width:157px;height:154px;background:var(--white);box-shadow:0 3px 14px rgba(0,0,0,.06);text-align:center;font-size:13.5px;font-weight:500;color:var(--teal);line-height:18px}
.icon-card svg{display:block;margin:28px auto 14px}
.arrow-sq{position:absolute;width:18px;height:28px;background:var(--teal);color:var(--white);display:flex;align-items:center;justify-content:center;font-size:12px}
.dots{position:absolute;top:302px;left:584px;display:flex;gap:7px}
.dots i{width:5px;height:5px;border-radius:50%;background:#cfe3e8;display:block}
.dots i.on{background:var(--teal)}

/* promise */
.promise{position:absolute;left:0;top:1645px;width:1200px;height:570px;background:linear-gradient(180deg,#1d8172 0%,#2a8f80 60%,#1a6e62 100%)}
.promise-title{position:absolute;top:56px;width:1200px;text-align:center;font-size:38px;font-weight:300;color:var(--white)}
.promise-title b{font-weight:700}
.promise-col{position:absolute;bottom:0;width:200px;height:100%}
.promise-col.feature{top:146px;height:424px;background:rgba(255,255,255,.12)}
.promise-label{position:absolute;width:200px;text-align:center;font-size:17px;line-height:22px;font-weight:300;color:var(--white)}

/* help */
.help-diagram{position:absolute;left:0;top:2440px;width:1200px;height:380px}
.node{position:absolute;width:62px;height:62px;border-radius:50%;background:var(--teal);border:5px solid #d7f0f5;display:flex;align-items:center;justify-content:center}
.role{position:absolute;font-size:12px;color:var(--ink)}
.done-btn{position:absolute;left:428px;top:2865px;width:344px;height:56px;background:var(--teal-light);color:var(--white);display:flex;align-items:center;justify-content:center;font-size:20px;letter-spacing:.5px}

/* services */
.services{position:absolute;left:0;top:2960px;width:1200px;height:583px;background:linear-gradient(180deg,#ffffff 0%,#f1f5f7 55%,#ffffff 100%)}
.svc-card{position:absolute;top:187px;width:274px;height:220px;background:var(--white);box-shadow:0 3px 14px rgba(0,0,0,.06)}
.svc-card .ph{width:100%;height:170px}
.svc-card span{display:block;text-align:center;margin-top:14px;font-size:16px;color:var(--teal)}

/* faq */
.faq-photo{position:absolute;left:102px;top:3639px;width:435px;height:380px;border-radius:50%;background:radial-gradient(circle at 55% 50%,#5c9a43 0%,#b8d69a 28%,#eef5f7 60%,#ffffff 80%)}
.faq-title{position:absolute;left:598px;top:3628px;font-size:38px;font-weight:300;color:var(--teal);line-height:46px}
.faq-title b{display:block;font-weight:700;color:var(--ink)}
.faq-q{position:absolute;left:598px;width:430px;font-size:14px;font-weight:700;color:var(--ink);line-height:23px}
.faq-a{position:absolute;left:598px;width:440px;font-size:14px;color:var(--muted);line-height:23px}

/* footer */
.footer{position:absolute;left:0;top:4199px;width:1200px;height:574px;background:var(--footer);color:#c9ccd3}
.subscribe{position:absolute;left:157px;top:4134px;width:884px;height:129px;background:var(--teal-light)}
.subscribe h3{position:absolute;left:50px;top:42px;font-size:36px;font-weight:300;color:var(--white)}
.subscribe h3 b{font-weight:700}
.sub-input{position:absolute;left:467px;top:40px;width:247px;height:48px;border:1px solid rgba(255,255,255,.7);color:rgba(255,255,255,.8);font-size:12px;display:flex;align-items:center;padding-left:14px}
.sub-btn{position:absolute;left:714px;top:40px;width:112px;height:48px;background:var(--white);color:var(--teal);font-size:13px;display:flex;align-items:center;justify-content:center}
.f-brand{position:absolute;left:87px;top:170px;display:flex;align-items:center;gap:10px;font-size:22px;font-weight:700;color:var(--teal)}
.f-brand i{width:28px;height:28px;border-radius:50%;background:var(--teal);display:block}
.f-about{position:absolute;left:87px;top:302px;width:280px;font-size:12.5px;line-height:24px}
.f-head{position:absolute;top:155px;font-size:20px;color:var(--white)}
.f-links{position:absolute;left:441px;top:216px;list-style:none;font-size:13px}
.f-links li{height:32px}
.post{position:absolute;left:644px;display:flex;gap:12px;font-size:11.5px;line-height:14px;color:var(--white)}
.post .thumb{width:66px;height:50px;background:linear-gradient(135deg,#7f8ea0,#c9d3dd)}
.post small{display:block;margin-top:5px;color:#c9ccd3;font-size:11px}
.f-btn{position:absolute;left:933px;width:144px;height:42px;border:1px solid #c9ccd3;border-radius:22px;display:flex;align-items:center;justify-content:center;font-size:13px;color:var(--white)}
.socials{position:absolute;left:540px;top:512px;display:flex;gap:26px}
.socials i{width:16px;height:16px;border-radius:50%;background:#d3d6dc;display:block}
.copy{position:absolute;left:92px;top:518px;font-size:11.5px}
.legal{position:absolute;left:922px;top:518px;font-size:11.5px}
</style>
</head>
<body>

<header class="site-header">
  <div class="brand"><i></i>Venture Z</div>
  <nav class="nav">
    <span class="home"><svg width="14" height="14" viewBox="0 0 14 14"><path d="M2 7L7 2l5 5M3.5 6v6h7V6" fill="none" stroke="#36cdc4" stroke-width="1.3"/></svg></span>
    <span>Services</span><span>About</span><span>Testimonials &amp; Press</span><span>Careers</span><span>Blog</span>
  </nav>
  <div class="btn btn-fill" style="left:848px;top:33px;width:143px;height:42px">Apply Now</div>
  <div class="btn btn-line" style="left:999px;top:33px;width:142px;height:42px">Get In Touch</div>
</header>

<section class="hero" role="img" aria-label="Bright office with people walking past glass walls, tinted teal">
  <h1 class="hero-title">Welcome to Venture Z</h1>
  <p class="hero-sub">The #1 leader in product development services, based in Silicon Valley, CA</p>
  <div class="btn btn-white" style="left:529px;top:292px;width:142px;height:42px">Get In Touch</div>
</section>

<div class="intro-card">
  <h3>Need help building a product?<span>We are here for you!</span></h3>
  <p>Venture Z works with companies of all sizes to design, build &amp; launch exceptional products from start to finish (and anywhere in between.) We take ideas from concept to launch, or can step into organizations that are experiencing product troubles and advise on how to clear roadblocks.</p>
</div>

<h2 class="work-title">We love to <b>work with:</b></h2>
<ul class="work-list">
  <li><svg width="12" height="10" viewBox="0 0 12 10"><path d="M1 5l3.5 3.5L11 1" fill="none" stroke="#29b3c9" stroke-width="1.8"/></svg>Entrepreneurs with an idea who wants to build a beta product or business</li>
  <li><svg width="12" height="10" viewBox="0 0 12 10"><path d="M1 5l3.5 3.5L11 1" fill="none" stroke="#29b3c9" stroke-width="1.8"/></svg>Start Up Companies who need a product built quickly and cost effectively</li>
  <li><svg width="12" height="10" viewBox="0 0 12 10"><path d="M1 5l3.5 3.5L11 1" fill="none" stroke="#29b3c9" stroke-width="1.8"/></svg>Small or medium sized, more established companies that are having issues shipping product</li>
  <li><svg width="12" height="10" viewBox="0 0 12 10"><path d="M1 5l3.5 3.5L11 1" fill="none" stroke="#29b3c9" stroke-width="1.8"/></svg>Larger sized companies that need Product Management consulting</li>
  <li><svg width="12" height="10" viewBox="0 0 12 10"><path d="M1 5l3.5 3.5L11 1" fill="none" stroke="#29b3c9" stroke-width="1.8"/></svg>Companies of all sizes that need great talent, quickly.</li>
</ul>
<div class="btn btn-fill" style="left:157px;top:1150px;width:143px;height:42px">Contact Us</div>
<div class="work-photo" role="img" aria-label="Two colleagues reviewing work on a laptop, framed in a round crop"></div>

<section class="excite">
  <h2 class="h2" style="top:58px">Things that <b>excite us:</b></h2>
  <div class="arrow-sq" style="left:121px;top:193px">‹</div>
  <div class="arrow-sq" style="left:1061px;top:193px">›</div>
  <div class="icon-card" style="left:157px"><svg width="52" height="52" viewBox="0 0 52 52"><circle cx="26" cy="26" r="14" fill="none" stroke="#1c1f26" stroke-width="2"/><circle cx="26" cy="26" r="5" fill="#29b3c9"/></svg>Innovation</div>
  <div class="icon-card" style="left:338px"><svg width="52" height="52" viewBox="0 0 52 52"><rect x="12" y="12" width="28" height="28" rx="4" fill="none" stroke="#1c1f26" stroke-width="2"/><circle cx="26" cy="26" r="6" fill="#29b3c9"/></svg>New design<br>&amp; technology</div>
  <div class="icon-card" style="left:519px"><svg width="52" height="52" viewBox="0 0 52 52"><circle cx="16" cy="18" r="6" fill="none" stroke="#1c1f26" stroke-width="2"/><circle cx="36" cy="30" r="6" fill="none" stroke="#1c1f26" stroke-width="2"/><path d="M16 26q4 14 20 12" fill="none" stroke="#29b3c9" stroke-width="2" stroke-dasharray="3 3"/></svg>Clear Roadmaps</div>
  <div class="icon-card" style="left:700px"><svg width="52" height="52" viewBox="0 0 52 52"><path d="M26 10q8 8 6 22h-12q-2-14 6-22z" fill="none" stroke="#29b3c9" stroke-width="2"/><circle cx="26" cy="22" r="3" fill="#29b3c9"/></svg>Product Releases</div>
  <div class="icon-card" style="left:881px"><svg width="52" height="52" viewBox="0 0 52 52"><circle cx="26" cy="15" r="6" fill="none" stroke="#29b3c9" stroke-width="2"/><path d="M17 30q9-8 18 0" fill="none" stroke="#29b3c9" stroke-width="2"/><path d="M10 40l3-6 3 6-6-3h6zM23 40l3-6 3 6-6-3h6zM36 40l3-6 3 6-6-3h6z" fill="none" stroke="#1c1f26" stroke-width="1.4"/></svg>Happy Clients</div>
  <div class="dots"><i></i><i class="on"></i><i></i></div>
</section>

<section class="promise" role="img" aria-label="Team members shaking hands and working together in an office, tinted green">
  <h2 class="promise-title">Things that <b>we promise:</b></h2>
  <div class="promise-col feature" style="left:400px"></div>
  <p class="promise-label" style="left:400px;top:324px">Great People<br>&amp; High Functioning<br>Teams</p>
  <p class="promise-label" style="left:0;top:479px">Experience,<br>Passion &amp; Impact</p>
  <p class="promise-label" style="left:200px;top:479px">Focused<br>strategies</p>
  <p class="promise-label" style="left:600px;top:479px">Integrity, Reliability<br>&amp; Security</p>
  <p class="promise-label" style="left:800px;top:479px">Data driven &amp; Design<br>centric results</p>
  <p class="promise-label" style="left:1000px;top:479px">Top customer service<br>for our clients</p>
</section>

<h2 class="h2" style="top:2296px">How Venture Z <b>Help You</b></h2>
<p class="lead" style="top:2358px">Lorem ipsum dolor sit amet, consectetur adipiscing elit, sed do eiusmod tempor incididunt ut labore et dolore magna aliqua. Ut enim ad minim veniam</p>

<div class="help-diagram">
  <svg class="abs" style="left:0;top:0" width="1200" height="380" viewBox="0 0 1200 380">
    <path d="M361 260 A237 237 0 0 1 835 260 Z" fill="#eef7fa"/>
    <g stroke="#8a9097" stroke-width="1" stroke-dasharray="4 4" fill="none">
      <line x1="596" y1="30" x2="598" y2="240"/>
      <line x1="426" y1="94" x2="540" y2="212"/>
      <line x1="772" y1="94" x2="656" y2="212"/>
      <line x1="363" y1="257" x2="508" y2="257"/>
      <line x1="688" y1="257" x2="835" y2="257"/>
    </g>
    <circle cx="598" cy="268" r="89" fill="#29b3c9"/>
    <circle cx="598" cy="268" r="70" fill="#ffffff"/>
    <circle cx="598" cy="268" r="58" fill="#29b3c9"/>
    <path d="M578 290h40v-22l-20-14-20 14z" fill="none" stroke="#fff" stroke-width="3"/>
    <path d="M598 228v40" stroke="#fff" stroke-width="3"/>
  </svg>
  <div class="node" style="left:565px;top:0"><svg width="26" height="26" viewBox="0 0 26 26"><rect x="4" y="5" width="18" height="14" rx="2" fill="none" stroke="#fff" stroke-width="2"/></svg></div>
  <div class="node" style="left:395px;top:64px"><svg width="26" height="26" viewBox="0 0 26 26"><path d="M8 8l-5 5 5 5M18 8l5 5-5 5" fill="none" stroke="#fff" stroke-width="2"/></svg></div>
  <div class="node" style="left:741px;top:64px"><svg width="26" height="26" viewBox="0 0 26 26"><circle cx="13" cy="9" r="4" fill="none" stroke="#fff" stroke-width="2"/><path d="M5 22q8-10 16 0" fill="none" stroke="#fff" stroke-width="2"/></svg></div>
  <div class="node" style="left:332px;top:226px"><svg width="26" height="26" viewBox="0 0 26 26"><path d="M6 20l10-10 4 4-10 10H6z" fill="none" stroke="#fff" stroke-width="2"/></svg></div>
  <div class="node" style="left:804px;top:226px"><svg width="26" height="26" viewBox="0 0 26 26"><circle cx="11" cy="11" r="6" fill="none" stroke="#fff" stroke-width="2"/><path d="M16 16l6 6" stroke="#fff" stroke-width="2"/></svg></div>
  <span class="role" style="left:575px;top:112px;transform:rotate(-90deg)">QA</span>
  <span class="role" style="left:448px;top:148px;transform:rotate(50deg)">Developers</span>
  <span class="role" style="left:640px;top:150px;transform:rotate(-50deg)">Product Managers</span>
  <span class="role" style="left:417px;top:263px">Designers</span>
  <span class="role" style="left:709px;top:263px">Researchers</span>
</div>
<div class="done-btn">FINALIZED PRODUCT DONE</div>

<section class="services">
  <h2 class="h2" style="top:40px">Our <b>Services</b></h2>
  <p class="lead" style="top:102px">Lorem ipsum dolor sit amet, consectetur adipiscing elit, sed do eiusmod tempor incididunt ut labore et dolore magna aliqua. Ut enim ad minim veniam</p>
  <div class="arrow-sq" style="left:121px;top:282px">‹</div>
  <div class="arrow-sq" style="left:1061px;top:282px">›</div>
  <div class="svc-card" style="left:157px"><div class="ph" role="img" aria-label="Hands working with digital interface graphics" style="background:linear-gradient(135deg,#2e4a5e,#7ea3b8)"></div><span>Research</span></div>
  <div class="svc-card" style="left:463px"><div class="ph" role="img" aria-label="Designer working at a desk with screens" style="background:linear-gradient(135deg,#c9d4dc,#6e8393)"></div><span>Design</span></div>
  <div class="svc-card" style="left:767px"><div class="ph" role="img" aria-label="Handshake in front of a city skyline" style="background:linear-gradient(135deg,#2d4f7a,#a3b9cf)"></div><span>Engineers</span></div>
  <div class="btn btn-fill" style="left:529px;top:446px;width:142px;height:42px">View More</div>
</section>

<div class="faq-photo" role="img" aria-label="Hands holding a small plant growing into a rising arrow"></div>
<h2 class="faq-title">Frequently Asked<b>Questions</b></h2>
<p class="faq-q" style="top:3744px">Lorem ipsum dolor sit amet, consectetur adipis cing elit, sed do eiusmod tempor</p>
<p class="faq-a" style="top:3808px">Lorem ipsum dolor sit amet, consectetur adipiscing elit, sed do eiusmod tempor incididunt ut labore et dolore</p>
<p class="faq-q" style="top:3878px">Lorem ipsum dolor sit amet, consectetur adipis cing elit, sed do eiusmod tempor</p>
<div class="btn btn-fill" style="left:599px;top:3966px;width:143px;height:42px">More Faq</div>

<footer class="footer">
  <div class="f-brand"><i></i>Venture Z</div>
  <p class="f-about">Lorem ipsum dolor sit amet, consectetur adipiscing elit, sed do eiusmod tempor incid idunt ut labore et dolore magna aliqua. Ut enim ad minim veniam</p>
  <h4 class="f-head" style="left:437px">Quick Links</h4>
  <ul class="f-links"><li>Home</li><li>Services</li><li>About</li><li>Testimonials &amp; Press</li><li>Careers</li><li>Blog</li></ul>
  <h4 class="f-head" style="left:643px">Blog</h4>
  <div class="post" style="top:218px"><div class="thumb"></div><div>Giving Back – Uganda<br>Training Centers<small>Jan 21, 2021</small></div></div>
  <div class="post" style="top:294px"><div class="thumb"></div><div>Giving Back – Uganda<br>Training Centers<small>Jan 21, 2021</small></div></div>
  <h4 class="f-head" style="left:933px;top:157px">Are You A Freelancer?</h4>
  <div class="f-btn" style="top:218px">Apply Here</div>
  <h4 class="f-head" style="left:933px;top:285px;line-height:26px">Do You Run Any<br>Company?</h4>
  <div class="f-btn" style="top:352px">Get In Touch</div>
  <p class="copy">© Copyright Venture Z All rights reserved.</p>
  <div class="socials"><i></i><i></i><i></i></div>
  <p class="legal">Privacy Policy &nbsp;&nbsp;|&nbsp;&nbsp; Terms &amp; Conditions</p>
</footer>

<div class="subscribe">
  <h3>Subscribe <b>to our blog</b></h3>
  <div class="sub-input">Enter Your Email</div>
  <div class="sub-btn">Submit</div>
</div>

</body>
</html>
```